Law Firm Needs a new Website Design

We need a new website design for our law firm located in Manhattan (Law Offices of Desmond T. Halvorsen, PLLC).
We have an existing logo that we will to continue using, which can be found in www.HalvorsenLegal.example.
The Peak Counsel, Premier Barristers Logo should also be reflected near the bottom of the Home page.
The website will be 6 pages.

Deliverables:
I want a
1) home page,
2) About Us/Practice Areas page,
3) attorneys,
4) News and Articles page, and
5) Contact and Directions/Privacy Policy page.

The colors of my logo should be in the website.
I also like a touch of black and red.

The website should project "excellence."
We seek to provide the highest quality legal services.
We handle estate planning, wills, trusts, planning for people with disabilities, asset protection and preservation, Medicaid planning, hospital safe discharge, nursing home placement, powers of attorney, health care proxies, living wills, guardianships, probate, estate administration and related litigation.

I would like the colors of my Logo used (including shading where appropriate).
I also want some black on the borders and/or bottom and some red touches throughout the page.

My Logo should appear everywhere that "Law Offices Of Desmond T. Halvorsen, PLLC" appears.
I want the badges for Peak counsel, Premier Barristers, Premier Legal Practices, and ZENLO on the Home page.
I do not want too much text on the home page.

We would also like the website to have coding.
The final design should also communicate quality, expertise and stability.
Great start so far by the people who submitted designs.
Thank you.

3276b5
ec1f27
474747

• Please use my logo each time you mention Law Offices of Desmond T. Halvorsen, PLLC. Please include the Peakcounsel, Premier Barristers, Premier Legal Practices and Zenlo rating Badges on the web home page. I only wish to be contacted by phone. I am not including testimonials and am only using the New York City address.
• Prefer illustrations to photos regarding practice areas
• Testimonials, contact me by email, free consultation.

```html
<!DOCTYPE html>
<html lang="en">
<head>
<meta charset="utf-8">
<title>Law Offices of Desmond T. Halvorsen, PLLC</title>
<link href="https://fonts.googleapis.com/css2?family=Noto+Serif:wght@400;700&family=Open+Sans:wght@400;600;700&display=swap" rel="stylesheet">
<style>
:root{
  --blue:#3276b5;
  --blue-dark:#1f3f73;
  --red:#ec1f27;
  --charcoal:#474747;
  --footer:#444444;
  --text:#333333;
  --light:#f7f7f9;
  --white:#ffffff;
  --serif:"Noto Serif", Georgia, serif;
  --sans:"Open Sans", Arial, sans-serif;
}
*{margin:0;padding:0;box-sizing:border-box}
html,body{width:1200px;height:2211px;overflow:hidden;background:var(--white)}
body{position:relative;font-family:var(--sans);color:var(--text)}
.abs{position:absolute}

/* header */
.site-header{position:absolute;left:0;top:0;width:1200px;height:46px;background:var(--white)}
.brand{position:absolute;left:250px;top:8px;display:flex;align-items:center;gap:8px}
.brand-mark{width:26px;height:26px;background:var(--blue-dark)}
.brand-name{font-family:var(--serif);font-size:13px;line-height:15px;color:var(--blue-dark);width:200px}
.header-phone{position:absolute;left:815px;top:8px;display:flex;align-items:center;gap:8px}
.phone-badge{width:30px;height:30px;border-radius:50%;background:var(--red);display:flex;align-items:center;justify-content:center}
.header-phone .label{font-family:var(--serif);font-size:10px;color:#555;line-height:11px}
.header-phone .number{font-family:var(--serif);font-size:15px;color:#333;line-height:17px}

.main-nav{position:absolute;left:0;top:46px;width:1200px;height:36px;background:var(--red);display:flex;justify-content:center;align-items:center;gap:28px}
.main-nav a{font-family:var(--serif);font-size:12.5px;color:var(--white);text-decoration:none}

/* hero */
.hero{position:absolute;left:0;top:82px;width:1200px;height:464px;overflow:hidden}
.hero-photo{position:absolute;inset:0;background:linear-gradient(135deg,#d9dde3 0%,#f1f2f4 40%,#c9ced6 100%)}
.hero-panel{position:absolute;inset:0}
.hero-rule{position:absolute;left:630px;top:105px;width:570px;height:2px;background:rgba(255,255,255,.8)}
.hero-title{position:absolute;left:628px;top:106px;font-family:var(--serif);font-size:52px;color:var(--white);font-weight:400}
.hero-text{position:absolute;left:628px;top:190px;width:305px;font-size:11px;line-height:18px;color:var(--white)}
.btn-red{position:absolute;background:var(--red);color:var(--white);font-family:var(--serif);font-size:14px;display:flex;align-items:center;justify-content:center;gap:6px}
.hero .btn-red{left:628px;top:294px;width:114px;height:26px}

/* section titles */
.section-title{position:absolute;left:0;width:1200px;text-align:center;font-family:var(--serif);font-size:20px;font-weight:400}
.divider{position:absolute;left:589px;width:22px;height:10px}

/* firm profile */
.profile-box{position:absolute;left:248px;top:546px;width:703px;height:166px;background:var(--light)}
.profile-text{position:absolute;left:256px;top:631px;width:688px;text-align:center;font-size:9.3px;line-height:13px;color:#444}

/* practice areas */
.practice{position:absolute;left:0;top:712px;width:1200px;height:470px;background:linear-gradient(120deg,#555 0%,var(--charcoal) 50%,#3d3d3d 100%)}
.practice .section-title{color:var(--white)}
.area-card{position:absolute;top:97px;width:224px}
.area-img{width:224px;height:137px;border:2px solid var(--red)}
.area-name{margin-top:12px;text-align:center;font-family:var(--serif);font-size:19px;color:var(--white)}
.area-text{margin-top:6px;text-align:justify;text-align-last:center;font-size:9.4px;line-height:13.3px;color:#e8e8e8}
.area-link{display:block;margin:8px auto 0;width:max-content;font-family:var(--serif);font-size:11px;color:var(--white);border-bottom:2px solid var(--red);padding-bottom:2px}

/* rating */
.rating{position:absolute;left:0;top:1209px;width:1200px;height:389px;background:linear-gradient(90deg,#e51d25 0%,var(--red) 60%,#d9161e 100%);overflow:hidden}
.rating-rule{position:absolute;left:0;height:2px;width:722px;background:rgba(255,255,255,.85)}
.rating-title{position:absolute;left:248px;top:52px;font-family:var(--sans);font-weight:700;font-size:28px;color:var(--white)}
.rating-text{position:absolute;left:248px;top:110px;width:318px;font-size:9.2px;line-height:17px;color:var(--white)}
.rating-call{position:absolute;left:248px;top:256px;display:flex;align-items:center;gap:4px;color:var(--white);font-size:18px}
.rating-phone{position:absolute;left:248px;top:285px;font-size:46px;font-weight:600;color:var(--white)}

/* news */
.news-card{position:absolute;top:1695px;width:224px;height:217px;background:#eeeeee}
.news-img{width:224px;height:109px;border:2px solid var(--red)}
.news-head{padding:7px 7px 0;font-family:var(--serif);font-weight:700;font-size:9px;line-height:12px;color:var(--blue)}
.news-text{padding:5px 7px 0;font-size:9px;line-height:11.5px;color:#333}

/* footer */
.site-footer{position:absolute;left:0;top:1935px;width:1200px;height:252px;background:var(--footer)}
.foot-title{position:absolute;top:22px;font-family:var(--serif);font-size:20px;color:var(--white);padding-bottom:6px;border-bottom:2px solid #6a6a6a}
.foot-links{position:absolute;left:248px;top:74px;list-style:none}
.foot-links li{font-size:15px;line-height:34px;color:var(--white)}
.foot-links li.current{color:var(--blue)}
.office-line{position:absolute;left:495px;display:flex;gap:6px;font-size:15px;line-height:21px;color:var(--white)}
.office-map{position:absolute;left:709px;top:78px;width:242px;height:148px;background:linear-gradient(135deg,#e8e3d3,#d8dcc9 50%,#e6e1cf);border:1px solid #999}
.bottom-bar{position:absolute;left:0;top:2187px;width:1200px;height:24px;background:var(--blue);color:var(--white);font-size:7.5px}
.bottom-bar span{position:absolute;left:248px;top:7px}
</style>
</head>
<body>

<header class="site-header">
  <div class="brand">
    <div class="brand-mark"></div>
    <div class="brand-name">Law Offices of Desmond T. Halvorsen, PLLC</div>
  </div>
  <div class="header-phone">
    <div class="phone-badge">
      <svg width="16" height="16" viewBox="0 0 24 24"><path fill="#fff" d="M6.6 10.8a15.1 15.1 0 0 0 6.6 6.6l2.2-2.2a1 1 0 0 1 1-.25 11.4 11.4 0 0 0 3.6.57 1 1 0 0 1 1 1V20a1 1 0 0 1-1 1A17 17 0 0 1 3 4a1 1 0 0 1 1-1h3.5a1 1 0 0 1 1 1c0 1.25.2 2.45.57 3.57a1 1 0 0 1-.25 1z"/></svg>
    </div>
    <div>
      <div class="label">Call Now</div>
      <div class="number">(555) 014-2270</div>
    </div>
  </div>
</header>

<nav class="main-nav">
  <a href="#">Home</a><a href="#">Practice Areas</a><a href="#">Privacy Policy</a><a href="#">Contact and Directions</a><a href="#">News</a>
</nav>

<section class="hero">
  <div class="hero-photo" role="img" aria-label="Photo of a lawyer's hand stamping a document beside a pen"></div>
  <svg class="hero-panel" width="1200" height="464" viewBox="0 0 1200 464">
    <defs>
      <linearGradient id="heroBlue" x1="0" y1="0" x2="1" y2="1">
        <stop offset="0" stop-color="#3a82c4"/><stop offset="1" stop-color="#2a67a5"/>
      </linearGradient>
    </defs>
    <polygon points="648,0 1200,0 1200,464 519,464" fill="url(#heroBlue)"/>
  </svg>
  <div class="hero-rule"></div>
  <h1 class="hero-title">Premier Barristers</h1>
  <p class="hero-text">Lorem Ipsum is simply dummy text of the printing and typesetting industry. Lorem Ipsum has been the industry's standard dummy text ever since the 1500s, when an unknown printer took a galley of type and scrambled it to make a type specimen book. It has survived not only five centuries</p>
  <a class="btn-red">Read More
    <svg width="9" height="10" viewBox="0 0 9 10"><path d="M2 1l4 4-4 4" fill="none" stroke="#fff" stroke-width="1.8"/></svg></a>
</section>

<section>
  <div class="profile-box"></div>
  <h2 class="section-title" style="top:568px;color:#333">Firm Profile</h2>
  <svg class="divider" style="top:599px" viewBox="0 0 22 10"><path d="M1 5l5-4 5 4-5 4z M11 5l5-4 5 4-5 4z" fill="none" stroke="#ec1f27" stroke-width="1.3"/></svg>
  <p class="profile-text">Our firm was founded in 1993 by Desmond T. Halvorsen, a member of the National Guild of Elder Counsel (NGEC) and an elder law practitioner for over 19 years. Our firm is uniquely positioned to provide quality legal advice and representation in regards to estate planning, wills, trusts, planning for people with disabilities, asset protection and preservation, Medicaid planning, hospital safe discharge, nursing home placement, powers of attorney, health care proxies, living wills, guardianships, probate, estate administration and related litigation</p>
</section>

<section class="practice" role="region" aria-label="Practice areas">
  <h2 class="section-title" style="top:30px">Pratice Areas</h2>
  <svg class="divider" style="top:60px" viewBox="0 0 22 10"><path d="M1 5l5-4 5 4-5 4z M11 5l5-4 5 4-5 4z" fill="none" stroke="#ec1f27" stroke-width="1.3"/></svg>

  <article class="area-card" style="left:248px">
    <div class="area-img" role="img" aria-label="Photo of a businessman holding a small model house" style="background:linear-gradient(180deg,#6d6d72,#9a9aa0 60%,#cfcfd2)"></div>
    <h3 class="area-name">Estate Planning</h3>
    <p class="area-text">Estate planning is not just for the very wealthy or for senior citizens and often does not focus solelyupon asset distribution after death. A comprehensive estate plan looks to maximize the benefits of one's assets while living and then to ensure that assets that remain</p>
    <a class="area-link">Read More ›</a>
  </article>
  <article class="area-card" style="left:488px">
    <div class="area-img" role="img" aria-label="Photo of a lawyer meeting with a couple across a desk" style="background:linear-gradient(135deg,#8a7a6a,#c9c3bb 55%,#e9e7e4)"></div>
    <h3 class="area-name">Residential Real Estate</h3>
    <p class="area-text">We handle all aspects of residential real estate transactions for both buyers and sellers. focus solelyupon asset distribution after death. A comprehensive estate plan looks to maximize the benefits of one's assets while living and then to ensure that assets that remain</p>
    <a class="area-link">Read More ›</a>
  </article>
  <article class="area-card" style="left:728px">
    <div class="area-img" role="img" aria-label="Photo of a gavel resting on a contract" style="background:linear-gradient(135deg,#4a2d22,#8a6a55 45%,#e4ddd3)"></div>
    <h3 class="area-name">Guardianships</h3>
    <p class="area-text">When an individual becomes incapacitated and if no advanced directives are in place, it might be necessary for family members or friends to bring a proceeding in New York State Supreme Court to have a guardian appointed for that person. The guardian can then manage</p>
    <a class="area-link">Read More ›</a>
  </article>

  <a class="btn-red" style="left:542px;top:413px;width:114px;height:26px;font-size:14px">More
    <svg width="11" height="11" viewBox="0 0 11 11"><path d="M5.5 1v9M1 5.5h9" stroke="#fff" stroke-width="2.2"/></svg></a>
</section>

<section class="rating">
  <div class="rating-rule" style="top:47px"></div>
  <div class="rating-rule" style="top:94px"></div>
  <h2 class="rating-title">Zenlo Rating Badges</h2>
  <p class="rating-text">Lorem Ipsum is simply dummy text of the printing and typesetting industry. Lorem Ipsum has been the industry's standard dummy text ever since the 1500s, when an unknown printer took a galley of type and scrambled it to make a type specimen book. It has survived not only five centuries, but also the leap into electronic typesetting, remaining essentially unchanged. It was popularised in the 1960s with the release of Lettrix sheets containing Lorem Ipsum passages, and more recently with desktop publishing software like Pagecraft Studio including versions of Lorem Ipsum.</p>
  <div class="rating-call">
    <svg width="20" height="22" viewBox="0 0 24 24"><path fill="#3276b5" d="M6.6 10.8a15.1 15.1 0 0 0 6.6 6.6l2.2-2.2a1 1 0 0 1 1-.25 11.4 11.4 0 0 0 3.6.57 1 1 0 0 1 1 1V20a1 1 0 0 1-1 1A17 17 0 0 1 3 4a1 1 0 0 1 1-1h3.5a1 1 0 0 1 1 1c0 1.25.2 2.45.57 3.57a1 1 0 0 1-.25 1z"/></svg>
    <span>Call Now</span>
  </div>
  <div class="rating-phone">(555) 013-8846</div>
  <svg class="abs" style="left:0;top:0" width="1200" height="389" viewBox="0 0 1200 389">
    <defs>
      <linearGradient id="scaleTone" x1="0" y1="0" x2="1" y2="1">
        <stop offset="0" stop-color="#f1d7a8"/><stop offset=".5" stop-color="#b07a45"/><stop offset="1" stop-color="#6a3f22"/>
      </linearGradient>
    </defs>
    <polygon points="774,0 985,0 1179,194 988,389 774,389 579,194" fill="url(#scaleTone)" role="img" aria-label="Photo of bronze scales of justice in a courtroom"/>
    <polyline points="774,0 579,194 774,389" fill="none" stroke="#3276b5" stroke-width="2"/>
  </svg>
</section>

<section>
  <h2 class="section-title" style="top:1634px;color:#333">Latest News</h2>
  <svg class="divider" style="top:1666px" viewBox="0 0 22 10"><path d="M1 5l5-4 5 4-5 4z M11 5l5-4 5 4-5 4z" fill="none" stroke="#ec1f27" stroke-width="1.3"/></svg>

  <article class="news-card" style="left:248px">
    <div class="news-img" role="img" aria-label="Photo of hands with glasses and pen over paperwork" style="background:linear-gradient(135deg,#f4f4f4,#cfd3d8)"></div>
    <h3 class="news-head">Mr. Halvorsen was selected for the 2015 New York's Peakcounsel listing</h3>
    <p class="news-text">Mr. Halvorsen was selected for inclusion in the 2012-2015 edition of The Premier Barristers in America in the practice of Elder Law. This edition was featured in Metro City Magazine Year-End Double Issue, as well as the Gotham Legal Journal</p>
  </article>
  <article class="news-card" style="left:488px">
    <div class="news-img" role="img" aria-label="Photo of joined hands over business documents" style="background:linear-gradient(135deg,#f2f2f2,#e3c9b8 55%,#d8dbe3)"></div>
    <h3 class="news-head">Mr. Halvorsen was selected for the 2015 New York Area's Top Rated Lawyers</h3>
    <p class="news-text">Mr. Halvorsen was selected for inclusion in the 2012-2015 edition of The Premier Barristers in America in the practice of Elder Law. This edition was featured in Metro City Magazine Year-End Double Issue, as well as the Gotham Legal Journal</p>
  </article>
  <article class="news-card" style="left:728px">
    <div class="news-img" role="img" aria-label="Photo of a lawyer reading a book before shelves of law volumes" style="background:linear-gradient(135deg,#7a4a22,#b98a52 50%,#3a3a3a)"></div>
    <h3 class="news-head">Mr. Halvorsen was Selected for the 2015 Premier Barristers in America in the practice of</h3>
    <p class="news-text">Mr. Halvorsen was selected for inclusion in the 2012-2015 edition of The Premier Barristers in America in the practice of Elder Law. This edition was featured in Metro City Magazine Year-End Double Issue, as well as the Gotham Legal Journal</p>
  </article>
</section>

<footer class="site-footer">
  <h3 class="foot-title" style="left:248px;width:110px">Site Map</h3>
  <ul class="foot-links">
    <li class="current">Home</li><li>Practice Areas</li><li>Privacy Policy</li><li>Contact and Directions</li><li>News</li>
  </ul>
  <h3 class="foot-title" style="left:495px;width:110px">Main office</h3>
  <div class="office-line" style="top:94px">
    <svg width="12" height="18" viewBox="0 0 12 18"><path d="M6 0a6 6 0 0 0-6 6c0 4.5 6 12 6 12s6-7.5 6-12a6 6 0 0 0-6-6zm0 8.5A2.5 2.5 0 1 1 6 3.5a2.5 2.5 0 0 1 0 5z" fill="#3276b5"/></svg>
    <span>218 Harbor Lane, Suite<br>1406New York,<br>&nbsp;New York 10099</span>
  </div>
  <div class="office-line" style="top:163px">
    <svg width="15" height="16" viewBox="0 0 24 24"><path fill="#3276b5" d="M6.6 10.8a15.1 15.1 0 0 0 6.6 6.6l2.2-2.2a1 1 0 0 1 1-.25 11.4 11.4 0 0 0 3.6.57 1 1 0 0 1 1 1V20a1 1 0 0 1-1 1A17 17 0 0 1 3 4a1 1 0 0 1 1-1h3.5a1 1 0 0 1 1 1c0 1.25.2 2.45.57 3.57a1 1 0 0 1-.25 1z"/></svg>
    <span>(555) 013-8846</span>
  </div>
  <div class="office-line" style="top:206px">
    <svg width="16" height="16" viewBox="0 0 16 16"><rect x="1" y="5" width="14" height="10" rx="1.5" fill="#3276b5"/><rect x="4" y="1" width="8" height="5" fill="none" stroke="#3276b5" stroke-width="1.5"/><rect x="4" y="8" width="8" height="4" fill="#444"/></svg>
    <span>(555) 014-2270</span>
  </div>
  <div class="office-map" role="img" aria-label="Street map showing the office location in Manhattan"></div>
</footer>

<div class="bottom-bar"><span>Copyright © 2016</span></div>

</body>
</html>
```